Outdoor sign for Brightwater Auto Restoration

I need a horizontal 4'x 8' outdoor roadside sign for my classic auto restoration business. I have uploaded colors and our logo. Needs the Brightwater name, a prominent Classic AUTO RESTORATION, phone number and website. We rebuild and restore vintage cars, trucks and 4x4s. I'd like something clean but possibly retro. Classic Auto Restoration is more important than the Brightwater name. It needs to be visible and readable from the street. NO CLIP ART

Target Market(s)

Customers who need their vintage care restored or upgraded. Men and women ages 25-75

Industry/Entity Type

Automotive

Colors
FFC000
F8CF3A
FAE287
FDF2CF
FEFAEE

Requirements
Must have
• Legible. Bright. Readable as a backlit 4' x 8' large horizontal sign (roughly 120cm X 240cm)
Nice to have
• Use of the Brightwater logo/type, Complete or Classic before prominent AUTO RESTORATION
Should not have
• Clip art of old cars or icons. And we don't want the Brightwater Logo from the website because it wont be legible from the road. I have included the Illustrator file for Brightwater text in the uploads

```html
<!DOCTYPE html>
<html lang="en">
<head>
<meta charset="utf-8">
<title>Brightwater Auto Restoration – Roadside Sign</title>
<link href="https://fonts.googleapis.com/css2?family=Graduate&family=Saira+Condensed:wght@700;800&family=Saira+Semi+Condensed:wght@700&display=swap" rel="stylesheet">
<style>
  :root{
    --frame:#3b3a2e;
    --gold:#f5ae1f;
    --gold-light:#f8cf3a;
    --stripe:#fae287;
    --stripe-pale:#fdf2cf;
    --navy:#0f2355;
    --charcoal:#343434;
    --white:#fefaee;
  }
  html,body{margin:0;padding:0;overflow:hidden;background:#fff;}
  .sign{display:block;width:1200px;height:600px;}
  .brand-name{font-family:"Saira Condensed",sans-serif;font-weight:800;fill:var(--navy);}
  .headline-classic{font-family:"Graduate",serif;fill:var(--charcoal);stroke:var(--white);stroke-width:5px;paint-order:stroke;}
  .headline-main{font-family:"Graduate",serif;fill:var(--navy);stroke:var(--white);stroke-width:6px;paint-order:stroke;}
  .contact-text{font-family:"Saira Semi Condensed",sans-serif;font-weight:700;fill:var(--charcoal);stroke:var(--white);stroke-width:3px;paint-order:stroke;}
  .icon-disc{fill:var(--navy);stroke:var(--white);stroke-width:3px;}
  .icon-line{fill:none;stroke:var(--white);stroke-width:3.5px;stroke-linecap:round;}
</style>
</head>
<body>
<svg class="sign" viewBox="0 0 1200 600" xmlns="http://www.w3.org/2000/svg">
  <!-- frame and panel -->
  <rect class="sign-frame" x="0" y="0" width="1200" height="600" fill="var(--frame)"/>
  <rect class="sign-panel" x="14" y="14" width="1172" height="572" fill="var(--gold)"/>

  <!-- contact stripe band -->
  <g class="contact-band" opacity="0.75">
    <rect x="14" y="409" width="1172" height="150" fill="var(--gold-light)"/>
    <rect x="14" y="411" width="1172" height="6" fill="var(--stripe-pale)"/>
    <rect x="14" y="423" width="1172" height="8" fill="var(--stripe-pale)"/>
    <rect x="14" y="437" width="1172" height="10" fill="var(--stripe-pale)"/>
    <rect x="14" y="453" width="1172" height="12" fill="var(--stripe-pale)"/>
    <rect x="14" y="471" width="1172" height="14" fill="var(--stripe-pale)"/>
    <rect x="14" y="491" width="1172" height="14" fill="var(--stripe-pale)"/>
    <rect x="14" y="511" width="1172" height="14" fill="var(--stripe-pale)"/>
    <rect x="14" y="531" width="1172" height="12" fill="var(--stripe-pale)"/>
    <rect x="14" y="549" width="1172" height="8" fill="var(--stripe-pale)"/>
  </g>

  <!-- brand name -->
  <text class="brand-name" x="600" y="108" text-anchor="middle" font-size="84" textLength="430" lengthAdjust="spacingAndGlyphs">BRIGHTWATER</text>

  <!-- headline -->
  <text class="headline-classic" x="592" y="256" text-anchor="middle" font-size="86" textLength="346" lengthAdjust="spacingAndGlyphs">CLASSIC</text>
  <text class="headline-main" x="610" y="378" text-anchor="middle" font-size="124" textLength="1088" lengthAdjust="spacingAndGlyphs">AUTO RESTORATION</text>

  <!-- phone -->
  <g class="contact-phone">
    <circle class="icon-disc" cx="363" cy="450" r="35"/>
    <path d="M350 433 l7 -3 l6 11 l-5 4 q3 9 11 14 l5 -4 l10 7 l-3 7 q-4 4 -12 1 q-18 -9 -22 -27 q-1 -7 3 -10z" fill="var(--white)"/>
    <path class="icon-line" d="M369 440 q6 2 8 8"/>
    <path class="icon-line" d="M371 431 q12 4 15 16"/>
    <text class="contact-text" x="413" y="472" font-size="62" textLength="450" lengthAdjust="spacingAndGlyphs">501-555-0142</text>
  </g>

  <!-- website -->
  <g class="contact-web">
    <circle class="icon-disc" cx="231" cy="527" r="34"/>
    <g class="icon-line" stroke-width="2.5">
      <circle cx="231" cy="527" r="19"/>
      <ellipse cx="231" cy="527" rx="8" ry="19"/>
      <line x1="231" y1="508" x2="231" y2="546"/>
      <line x1="212" y1="527" x2="250" y2="527"/>
      <line x1="215" y1="517" x2="247" y2="517"/>
      <line x1="215" y1="537" x2="247" y2="537"/>
    </g>
    <text class="contact-text" x="277" y="545" font-size="46" textLength="760" lengthAdjust="spacingAndGlyphs">WWW.BRIGHTWATERAUTOWORKS.COM</text>
  </g>
</svg>
</body>
</html>
```